Varlo Build for Rent Development Company

We are a new multifamily, build for rent, development company that is looking to build a pitch book outlining our company along with the real estate opportunity. We would want the style to be a modern, clean aesthetic with cool colors

```html
<!DOCTYPE html>
<html lang="en">
<head>
<meta charset="utf-8">
<title>Varlo Pitch Book</title>
<link href="https://fonts.googleapis.com/css2?family=Inter:wght@400;500;600;700&display=swap" rel="stylesheet">
<style>
:root{
  --board:#1c1c1c;
  --navy:#22264a;
  --navy-deep:#1f2244;
  --gold:#dfbb6e;
  --grey-row:#e9eaee;
  --halo:#ecedf1;
  --ink:#1d1f33;
  --text:#555866;
  --white:#ffffff;
}
*{margin:0;padding:0;box-sizing:border-box}
html,body{width:1029px;height:1200px;overflow:hidden;background:var(--board)}
body{font-family:'Inter',Arial,sans-serif;position:relative}
.board{position:absolute;left:0;top:0;width:1777px;height:2072px;transform:scale(.57907);transform-origin:0 0}
.slide{position:absolute;width:791px;height:443px;background:var(--white);overflow:hidden}
.title-band{position:absolute;left:0;top:21px;width:481px;height:49px;background:var(--navy);border-radius:0 25px 25px 0;color:var(--white);font-size:22px;font-weight:500;letter-spacing:.2px;padding-left:41px;line-height:49px}
.page-no{position:absolute;left:41px;top:411px;font-size:9px;font-weight:600;color:var(--ink)}
.wordmark{position:absolute;right:42px;top:398px;font-size:22px;font-weight:500;color:var(--navy);letter-spacing:.5px}
svg.icon{position:absolute}
.abs{position:absolute}

/* cover */
.cover{background:var(--navy)}
.cover .photo{position:absolute;inset:0;background:linear-gradient(180deg,#c98a7a 0%,#8a6a86 22%,#3b3a5c 48%,#2a2c52 70%,#25284f 100%)}
.cover .brand{position:absolute;top:299px;width:100%;text-align:center;color:var(--gold);font-size:20px;font-weight:500}
.cover h1{position:absolute;top:326px;width:100%;text-align:center;color:var(--white);font-size:38px;font-weight:500;letter-spacing:.3px}
.cover p{position:absolute;top:380px;width:100%;text-align:center;color:var(--white);font-size:14px;line-height:22px}

/* strategy */
.halo{position:absolute;border-radius:50%;background:var(--halo)}
.photo-round{position:absolute;border-radius:50%;border:3px solid var(--white)}
.node{position:absolute;width:64px;height:64px;border-radius:50%}
.node.navy{background:var(--navy)}
.node.gold{background:var(--gold)}
.node svg{position:absolute;left:16px;top:16px}
.node-label{position:absolute;font-size:14.5px;line-height:21px;color:var(--text)}
.node-label.right{text-align:right}

/* toc */
.toc{position:absolute;left:254px;top:107px}
.toc li{list-style:none;display:flex;height:38px;line-height:20px;font-size:13px;color:var(--text)}
.toc .num{width:53px;font-weight:600;color:var(--ink)}

/* table */
.econ-table{position:absolute;left:87px;top:101px;width:617px;border-radius:12px;overflow:hidden;box-shadow:0 4px 14px rgba(30,34,70,.12);background:var(--white)}
.econ-table .row{display:flex;height:59px}
.econ-table .head{height:44px}
.econ-table .c1{width:222px;padding-left:31px;display:flex;align-items:center;font-size:11.5px;font-weight:500;color:var(--ink);border-right:1px solid #d8d9df}
.econ-table .c2{flex:1;padding:0 30px 0 35px;display:flex;align-items:center;font-size:10px;line-height:19px;color:var(--text)}
.econ-table .head .c1{background:var(--gold);color:var(--white);font-size:15px;font-weight:600}
.econ-table .head .c2{background:var(--navy);color:var(--white);font-size:15px;font-weight:600}
.econ-table .row.shade{background:var(--grey-row)}

/* who */
.who-lead{position:absolute;top:106px;width:100%;text-align:center;font-size:12px;font-weight:600;color:var(--ink)}
.who-copy{position:absolute;left:110px;width:571px;text-align:center;font-size:11.6px;line-height:21.5px;color:var(--text)}
.value-item{position:absolute;top:306px;width:120px;margin-left:-60px;text-align:center}
.value-item .dot{width:56px;height:56px;border-radius:50%;background:var(--gold);margin:0 auto;position:relative;box-shadow:0 2px 6px rgba(0,0,0,.12)}
.value-item .dot svg{position:absolute;left:12px;top:12px}
.value-item span{display:block;margin-top:12px;font-size:12px;font-weight:500;color:var(--ink)}

/* drivers */
.drivers-copy{position:absolute;left:42px;top:107px;width:337px;font-size:10.2px;line-height:19.5px;color:var(--text);text-align:justify}
.drivers-copy p{margin-bottom:19px}
.drivers-copy .lead{color:var(--ink);font-weight:600;text-align:left}
.bar{position:absolute;left:415px;width:317px;height:25px;border-radius:13px;background:var(--white);box-shadow:0 2px 8px rgba(30,34,70,.1)}
.bar .fill{height:100%;border-radius:13px}
.bar .fill.gold{background:var(--gold)}
.bar .fill.navy{background:var(--navy)}
.bar .pct{position:absolute;right:12px;top:7px;font-size:8px;font-weight:600;color:var(--ink)}

/* market */
.market-copy{position:absolute;left:42px;top:104px;width:335px;font-size:12px;line-height:23px;color:var(--text);text-align:justify}
.market-copy p{margin-bottom:23px}
.pull-quote{position:absolute;left:57px;top:313px;border-left:3px solid var(--gold);padding-left:22px;width:310px;font-size:12px;line-height:20px;font-weight:600;color:var(--ink)}

/* closing */
.closing{background:var(--navy-deep)}
.closing .photo{position:absolute;inset:0;background:linear-gradient(180deg,#2a2e55 0%,#262a52 55%,#20234a 100%)}
.closing .chat{position:absolute;left:343px;top:27px;width:92px;height:92px;border-radius:50%;background:var(--gold)}
.closing .chat svg{position:absolute;left:22px;top:24px}
.closing h2{position:absolute;top:132px;width:100%;text-align:center;color:var(--white);font-size:40px;line-height:47px;font-weight:500}
.closing .kicker{position:absolute;top:236px;width:100%;text-align:center;color:var(--white);font-size:10.5px;font-weight:600}
.contact{position:absolute;top:278px;width:200px;margin-left:-100px;text-align:center;color:var(--white);font-size:13px;line-height:22px}
.contact .ring{width:58px;height:58px;border-radius:50%;background:var(--white);margin:0 auto 18px;position:relative}
.contact .ring svg{position:absolute;left:13px;top:13px}
</style>
</head>
<body>
<div class="board">

  <!-- Cover -->
  <section class="slide cover" style="left:67px;top:58px">
    <div class="photo" role="img" aria-label="Dusk photograph of a modern multifamily apartment building"></div>
    <div class="brand">VARLO</div>
    <h1>MULTIFAMILY. BUILT FOR RENT.</h1>
    <p>A modern development platform creating high-quality rental communities<br>designed for durable, long-term value.</p>
  </section>

  <!-- Development strategy -->
  <section class="slide" style="left:921px;top:58px">
    <div class="title-band">DEVELOPMENT STRATEGY</div>
    <div class="halo" style="left:233px;top:100px;width:296px;height:296px"></div>
    <div class="photo-round" role="img" aria-label="Photograph of a four-storey apartment building under blue sky" style="left:269px;top:136px;width:224px;height:224px;background:linear-gradient(180deg,#3f86c9 0%,#8fb9de 45%,#8a6f5a 70%,#4c6a3c 100%)"></div>

    <div class="node navy" style="left:224px;top:112px">
      <svg width="32" height="32" viewBox="0 0 32 32" fill="none" stroke="#dfbb6e" stroke-width="1.5"><circle cx="16" cy="9" r="6"/><path d="M10 9h12M16 3c-3 4-3 8 0 12M16 3c3 4 3 8 0 12"/><path d="M5 29V21M11 29V18M17 29V20M23 29V16M28 29H3"/></svg>
    </div>
    <div class="node gold" style="left:476px;top:112px">
      <svg width="32" height="32" viewBox="0 0 32 32" fill="none" stroke="#22264a" stroke-width="1.5"><circle cx="16" cy="16" r="13"/><path d="M16 7l7 5-3 9h-8l-3-9z"/></svg>
    </div>
    <div class="node gold" style="left:169px;top:219px">
      <svg width="32" height="32" viewBox="0 0 32 32" fill="none" stroke="#22264a" stroke-width="1.5"><path d="M9 12h14l3 17H6z"/><path d="M12 12V8a4 4 0 0 1 8 0v4"/><path d="M18 17c-1-1-4-1-4 1s4 1 4 3-3 2-4 1M16 15v9"/></svg>
    </div>
    <div class="node navy" style="left:531px;top:219px">
      <svg width="32" height="32" viewBox="0 0 32 32" fill="none" stroke="#dfbb6e" stroke-width="1.5"><circle cx="12" cy="12" r="6"/><circle cx="12" cy="12" r="2"/><circle cx="21" cy="21" r="7"/><circle cx="21" cy="21" r="2.5"/></svg>
    </div>
    <div class="node navy" style="left:224px;top:326px">
      <svg width="32" height="32" viewBox="0 0 32 32" fill="none" stroke="#dfbb6e" stroke-width="1.5"><path d="M7 3h13l5 5v12M7 3v26h12"/><path d="M11 11h9M11 16h9M11 21h5"/><circle cx="23" cy="25" r="5"/><path d="M21 25l1.5 1.5L25 24"/></svg>
    </div>
    <div class="node gold" style="left:476px;top:326px">
      <svg width="32" height="32" viewBox="0 0 32 32" fill="none" stroke="#22264a" stroke-width="1.5"><circle cx="11" cy="19" r="8"/><path d="M13 15c-1-1-4-1-4 1s4 1 4 3-3 2-4 1M11 13v12"/><rect x="20" y="10" width="9" height="18" rx="1"/><path d="M22 14h5M22 19h5M22 23h5"/></svg>
    </div>

    <div class="node-label right" style="right:585px;top:121px">Target High-Growth<br>Markets</div>
    <div class="node-label" style="left:558px;top:121px">Create Differentiated<br>Communities</div>
    <div class="node-label right" style="right:640px;top:228px">Design<br>for Demand</div>
    <div class="node-label" style="left:613px;top:228px">Build Long-Term<br>Value</div>
    <div class="node-label right" style="right:585px;top:335px">Acquire Strategic<br>Sites</div>
    <div class="node-label" style="left:558px;top:335px">Control Development<br>Costs</div>

    <div class="page-no">Page 05 of 08</div>
    <div class="wordmark">VARLO</div>
  </section>

  <!-- Table of contents -->
  <section class="slide" style="left:67px;top:562px">
    <div class="title-band">TABLE OF CONTENTS</div>
    <ul class="toc">
      <li><span class="num">01</span>Introduction</li>
      <li><span class="num">02</span>Table Of Contents (Agenda)</li>
      <li><span class="num">03</span>Who We Are</li>
      <li><span class="num">04</span>Market Opportunity</li>
      <li><span class="num">05</span>Development Strategy</li>
      <li><span class="num">06</span>Economic Model</li>
      <li><span class="num">07</span>Value Creation Drivers</li>
      <li><span class="num">08</span>Thank You</li>
    </ul>
    <div class="page-no">Page 02 of 08</div>
    <div class="wordmark">VARLO</div>
  </section>

  <!-- Economic model -->
  <section class="slide" style="left:921px;top:562px">
    <div class="title-band">ECONOMIC MODEL</div>
    <div class="econ-table">
      <div class="row head"><div class="c1">ECONOMIC MODEL</div><div class="c2">VALUE CREATION</div></div>
      <div class="row shade"><div class="c1">LAND ACQUISITION</div><div class="c2">Ut enim ad minima veniam, quis nostrum exercitationem ullam corporis suscipit laboriosam, nisi ut aliquid ex ea</div></div>
      <div class="row"><div class="c1">DEVELOPMENT</div><div class="c2">Ut enim ad minima veniam, quis nostrum exercitationem ullam corporis suscipit laboriosam, nisi ut aliquid ex ea</div></div>
      <div class="row shade"><div class="c1">STABILIZATION</div><div class="c2">Ut enim ad minima veniam, quis nostrum exercitationem ullam corporis suscipit laboriosam, nisi ut aliquid ex ea</div></div>
      <div class="row"><div class="c1">LONG-TERM VALUE</div><div class="c2">Ut enim ad minima veniam, quis nostrum exercitationem ullam corporis suscipit laboriosam, nisi ut aliquid ex ea</div></div>
    </div>
    <div class="page-no">Page 06 of 08</div>
    <div class="wordmark">VARLO</div>
  </section>

  <!-- Who we are -->
  <section class="slide" style="left:67px;top:1066px">
    <div class="title-band">WHO WE ARE</div>
    <div class="who-lead">Building places people are proud to call home.</div>
    <p class="who-copy" style="top:147px">Varlo is a multifamily and build-to-rent development company focused on creating thoughtfully designed communities in high-growth markets. We combine disciplined real estate fundamentals with a modern approach to design, development, and resident experience.</p>
    <p class="who-copy" style="top:233px">Our focus is simple: identify the right opportunities, build with purpose, and create long-term value for residents, partners, and investors.</p>
    <div class="value-item" style="left:206px">
      <div class="dot"><svg width="32" height="32" viewBox="0 0 32 32" fill="none" stroke="#22264a" stroke-width="1.5"><circle cx="16" cy="16" r="12"/><path d="M11 22h10M12 22l1-8h6l1 8M13 14l-1-4 4 2 4-2-1 4"/></svg></div>
      <span>Strategic</span>
    </div>
    <div class="value-item" style="left:318px">
      <div class="dot"><svg width="32" height="32" viewBox="0 0 32 32" fill="none" stroke="#22264a" stroke-width="1.5"><circle cx="16" cy="16" r="12"/><circle cx="16" cy="16" r="7"/><path d="M12.5 16l2.5 2.5 4.5-5"/></svg></div>
      <span>Disciplined</span>
    </div>
    <div class="value-item" style="left:445px">
      <div class="dot"><svg width="32" height="32" viewBox="0 0 32 32" fill="none" stroke="#22264a" stroke-width="1.5"><circle cx="16" cy="16" r="12"/><circle cx="16" cy="13" r="3.5"/><path d="M10 22c1.5-3.5 10.5-3.5 12 0"/><path d="M16 2v4M16 26v4M2 16h4M26 16h4"/></svg></div>
      <span>Resident-Focused</span>
    </div>
    <div class="value-item" style="left:576px">
      <div class="dot"><svg width="32" height="32" viewBox="0 0 32 32" fill="none" stroke="#22264a" stroke-width="1.5"><path d="M4 10V4h6M22 4h6v6M28 22v6h-6M10 28H4v-6M4 4l7 7M28 4l-7 7M28 28l-7-7M4 28l7-7"/><rect x="12" y="12" width="8" height="8"/></svg></div>
      <span>Built to Scale</span>
    </div>
    <div class="page-no">Page 03 of 08</div>
    <div class="wordmark">VARLO</div>
  </section>

  <!-- Value creation drivers -->
  <section class="slide" style="left:921px;top:1066px">
    <div class="title-band">VALUE CREATION DRIVERS</div>
    <div class="drivers-copy">
      <p class="lead">Varlo creates value through disciplined development, thoughtful design, and strong asset-level execution. Our strategy is focused on improving project economics from acquisition through stabilization while building communities with durable long-term appeal.</p>
      <p>Sed ut perspiciatis unde omnis iste natus error sit voluptatem accusantium doloremque laudantium, totam rem aperiam, eaque ipsa quae ab illo inventore veritatis et quasi architecto beatae vitae dicta sunt explicabo.</p>
      <p>Nemo enim ipsam voluptatem quia voluptas sit aspernatur aut odit aut fugit, sed quia consequuntur magni dolores eos qui ratione voluptatem sequi nesciunt.</p>
    </div>
    <div class="bar" style="top:108px"><div class="fill gold" style="width:56%"></div><span class="pct">60%</span></div>
    <div class="bar" style="top:146px"><div class="fill navy" style="width:70%"></div><span class="pct">80%</span></div>
    <div class="bar" style="top:185px"><div class="fill gold" style="width:42%"></div><span class="pct">40%</span></div>
    <div class="bar" style="top:223px"><div class="fill navy" style="width:33%"></div><span class="pct">30%</span></div>
    <div class="bar" style="top:261px"><div class="fill gold" style="width:65%"></div><span class="pct">70%</span></div>
    <div class="bar" style="top:300px"><div class="fill navy" style="width:55%"></div><span class="pct">60%</span></div>
    <div class="bar" style="top:338px"><div class="fill gold" style="width:78%"></div><span class="pct">70%</span></div>
    <div class="page-no">Page 07 of 08</div>
    <div class="wordmark">VARLO</div>
  </section>

  <!-- Market opportunity -->
  <section class="slide" style="left:65px;top:1570px">
    <div class="title-band">MARKET OPPORTUNITY</div>
    <div class="market-copy">
      <p>Sed ut perspiciatis unde omnis iste natus error sit voluptatem accusantium doloremque laudantium, totam rem aperiam, eaque ipsa quae ab illo inventore veritatis et quasi architecto beatae vitae dicta sunt explicabo. Nemo enim ipsam voluptatem quia voluptas sit aspernatur</p>
      <p>Neque porro quisquam est, qui dolorem ipsum quia dolor sit amet, consectetur, adipisci velit.</p>
    </div>
    <div class="pull-quote">We pursue markets and sites supported by strong population growth, employment, and housing fundamentals.</div>
    <div class="halo" style="left:383px;top:35px;width:380px;height:380px;background:radial-gradient(circle,#eef0f4 0%,#f6f7f9 60%,#ffffff 100%)"></div>
    <div class="photo-round" role="img" aria-label="Photograph of a three-storey townhouse building at twilight" style="left:427px;top:79px;width:292px;height:292px;background:linear-gradient(180deg,#5d86b8 0%,#7b93b3 35%,#4a5a78 65%,#2d3550 100%)"></div>
    <div class="page-no">Page 04 of 08</div>
    <div class="wordmark">VARLO</div>
  </section>

  <!-- Closing -->
  <section class="slide closing" style="left:920px;top:1570px">
    <div class="photo" role="img" aria-label="Faint navy-tinted photograph of a residential neighbourhood"></div>
    <div class="chat"><svg width="48" height="44" viewBox="0 0 48 44" fill="none" stroke="#ffffff" stroke-width="2.4"><path d="M6 4h26a4 4 0 0 1 4 4v14a4 4 0 0 1-4 4H16l-8 7v-7H6a4 4 0 0 1-4-4V8a4 4 0 0 1 4-4z"/><path d="M36 14h6a4 4 0 0 1 4 4v12a4 4 0 0 1-4 4h-2v6l-7-6H24"/></svg></div>
    <h2>LET’S BUILD THE FUTURE<br>OF RENTAL LIVING</h2>
    <div class="kicker">EXPLORE THE VARLO DEVELOPMENT &amp; INVESTMENT OPPORTUNITY</div>
    <div class="contact" style="left:212px">
      <div class="ring"><svg width="32" height="32" viewBox="0 0 32 32" fill="none" stroke="#22264a" stroke-width="1.5"><path d="M4 10l7-3 10 3 7-3v17l-7 3-10-3-7 3z"/><path d="M16 19s-5-5-5-8.5a5 5 0 0 1 10 0C21 14 16 19 16 19z"/><circle cx="16" cy="10.5" r="1.8"/></svg></div>
      1450 Harbor Lane, Suite 300<br>Denver, CO 80202, USA
    </div>
    <div class="contact" style="left:418px">
      <div class="ring"><svg width="32" height="32" viewBox="0 0 32 32" fill="none" stroke="#22264a" stroke-width="1.5"><rect x="4" y="9" width="24" height="18" rx="1"/><path d="M4 10l12 9 12-9"/><circle cx="16" cy="9" r="4"/></svg></div>
      Email Us:<br>info@varloadmin.com
    </div>
    <div class="contact" style="left:596px">
      <div class="ring"><svg width="32" height="32" viewBox="0 0 32 32" fill="none" stroke="#22264a" stroke-width="1.5"><circle cx="16" cy="16" r="12"/><path d="M4 16h24M16 4c-5 6-5 18 0 24M16 4c5 6 5 18 0 24M6 10h20M6 22h20"/></svg></div>
      Website:<br>www.Varlo.com
    </div>
  </section>

</div>
</body>
</html>
```